Bref créative
Healthcare apparel brand
Business Card, Letter head, Envelope, Email stationary
I need double sided standard sized Business Card [3.5" x 2"]
Bank Gothic and complimenting fonts
Professional
Marcus Pellandrou
CEO / Founder
482 Folwell Lane Suite B217
Harbor Vista, CA 93184
marcusp@brightloomwovens.example
www.veltunic.example
the corporation is Bright Loom Wovens LLC. The brand is Vel Tunic. I want to prominently display the green cross. Large. Maybe watermark. slogan "Fabrics That Care"
"A durable performance base layer that stays fresh and clean through every long shift." and either one of
"A better choice" or "Just what the doctor ordered"
Logo

```html
<!DOCTYPE html>
<html lang="en">
<head>
<meta charset="utf-8">
<title>Vel Tunic Stationery</title>
<link href="https://fonts.googleapis.com/css2?family=Michroma&family=Open+Sans:wght@400;600&display=swap" rel="stylesheet">
<style>
:root{
  --green:#7ab72d;
  --ink:#3d3d3d;
  --muted:#8a8a8a;
  --paper:#ffffff;
  --slate:#4b4b4d;
  --backdrop:#e9e6e1;
  --rule:#cfcfcf;
  --field:#d6d6d6;
}
*{box-sizing:border-box;margin:0;padding:0}
html,body{width:1200px;height:935px;overflow:hidden}
body{background:var(--backdrop);font-family:"Open Sans",sans-serif;color:var(--ink);position:relative}
.sheet{position:absolute;background:var(--paper);box-shadow:0 1px 4px rgba(0,0,0,.12)}
.brand{display:flex;align-items:center;gap:8px}
.brand-mark{background:var(--green);flex:none}
.brand-name{font-family:"Michroma",sans-serif;color:var(--ink);letter-spacing:.04em;white-space:nowrap}
.brand-sub{font-family:"Michroma",sans-serif;color:var(--green);letter-spacing:.18em;white-space:nowrap}
.slogan{font-family:"Michroma",sans-serif;letter-spacing:.1em;text-transform:uppercase;white-space:nowrap}

/* fax */
.fax{left:38px;top:150px;width:582px;height:760px;padding:70px 40px}
.fax .brand-name{font-size:19px}
.fax .brand-sub{font-size:7px;margin-top:4px}
.fax-title{font-family:"Michroma",sans-serif;font-weight:400;font-size:30px;margin:80px 0 50px}
.fax-field{display:flex;align-items:flex-end;height:36px;font-size:13px;font-weight:600}
.fax-field span{width:64px}
.fax-field i{width:100px;border-bottom:1px solid var(--rule)}
.fax-checks{display:flex;gap:22px;margin-top:30px;font-size:12px}
.fax-checks label{display:flex;align-items:center;gap:7px}
.fax-checks b{width:13px;height:13px;background:var(--field);display:inline-block}
.fax-foot{position:absolute;left:0;right:0;bottom:30px;height:4px;background:var(--green)}

/* letterhead */
.letterhead{left:260px;top:115px;width:520px;height:790px;padding:62px 36px}
.letterhead .head{display:flex;justify-content:space-between;align-items:flex-start}
.letterhead .brand-name{font-size:21px}
.letterhead .brand-sub{font-size:7.5px;margin-top:5px}
.contact{font-size:8.5px;line-height:1.6;color:var(--muted)}
.contact b{color:var(--ink);font-weight:600;display:inline-block;width:34px}
.watermark{position:absolute;left:110px;top:250px;width:260px;height:260px;background:var(--green);opacity:.08}
.letter-foot{position:absolute;left:0;right:0;bottom:24px}
.letter-foot .line{height:3px;background:var(--green)}
.letter-foot .slogan{text-align:right;font-size:10px;color:var(--green);padding:10px 30px 0}

/* envelope */
.envelope{left:523px;top:375px;width:534px;height:390px}
.envelope .flap-mark{position:absolute;left:252px;top:22px;width:30px;height:30px;background:var(--green)}
.envelope .brand{position:absolute;left:40px;top:125px}
.envelope .brand-name{font-size:24px}
.envelope .brand-sub{font-size:8px;margin-top:5px}
.envelope .return{position:absolute;left:92px;top:186px;font-size:9px;color:var(--muted)}
.envelope .band{position:absolute;left:0;right:0;bottom:22px;height:30px;background:var(--green);color:#fff;font-size:10px;text-align:right;padding:9px 150px 0 0}

/* cards */
.card{position:absolute;border-radius:10px;overflow:hidden;box-shadow:0 1px 4px rgba(0,0,0,.15)}
.card.light{background:var(--paper)}
.card.dark{background:var(--slate);color:#eee}
.card .band{position:absolute;left:0;right:0;bottom:0;height:22px;background:var(--green);color:#fff;font-size:8px;text-align:right;padding:7px 14px 0 0}
.card .thin{position:absolute;left:0;right:0;bottom:0;height:4px;background:var(--green)}
.card-brand .brand-name{font-size:13px}
.card-info{font-size:7.5px;line-height:1.55;color:var(--muted);margin-top:8px}
.card-info strong{color:var(--ink);font-weight:600;font-size:8.5px}
.card-front{left:930px;top:20px;width:258px;height:125px;padding:22px 18px}
.card-detail{left:808px;top:145px;width:249px;height:145px;padding:20px 18px}
.card-detail .brand-name{color:#fff}
.card-detail .card-info{color:#cfcfcf}
.card-detail .card-info strong{color:#fff}
.card-blurb{left:925px;top:645px;width:263px;height:148px;padding:24px 20px}
.card-blurb .url{font-size:9px;color:var(--ink);font-weight:600}
.card-blurb p{font-size:7.5px;line-height:1.6;color:var(--muted);margin-top:8px}
.card-back{left:808px;top:802px;width:267px;height:125px;padding:16px 20px}
.card-back .brand-name{color:#fff}
.card-back p{font-size:7.5px;line-height:1.6;color:#cfcfcf;margin-top:6px}
</style>
</head>
<body>

<section class="sheet fax">
  <div class="brand"><span class="brand-mark" style="width:22px;height:22px"></span><div><div class="brand-name">VEL TUNIC</div><div class="brand-sub">BRIGHT LOOM WOVENS</div></div></div>
  <h1 class="fax-title">FAX</h1>
  <div class="fax-field"><span>To :</span><i></i></div>
  <div class="fax-field"><span>Fax :</span><i></i></div>
  <div class="fax-field"><span>Phone :</span><i></i></div>
  <div class="fax-field"><span>Re :</span><i></i></div>
  <div class="fax-checks"><label><b></b>Urgent</label><label><b></b>Reply</label></div>
  <div class="fax-foot"></div>
</section>

<section class="sheet letterhead">
  <div class="watermark" role="img" aria-label="Faint brand square watermark"></div>
  <div class="head">
    <div class="brand"><span class="brand-mark" style="width:24px;height:24px"></span><div><div class="brand-name">VEL TUNIC</div><div class="brand-sub">BRIGHT LOOM WOVENS</div></div></div>
    <div class="contact">
      482 Folwell Lane Suite B217<br>Harbor Vista, CA 93184<br><br>
      <b>Phone</b> 805.555.0147<br>
      <b>Fax</b> 805.555.0148<br>
      <b>Email</b> marcusp@brightloomwovens.example<br>
      <b>Web</b> www.veltunic.example
    </div>
  </div>
  <div class="letter-foot"><div class="line"></div><div class="slogan">Fabrics That Care</div></div>
</section>

<section class="sheet envelope">
  <span class="flap-mark"></span>
  <div class="brand"><span class="brand-mark" style="width:24px;height:24px"></span><div><div class="brand-name">VEL TUNIC</div><div class="brand-sub">BRIGHT LOOM WOVENS</div></div></div>
  <div class="return">482 Folwell Lane Suite B217, Harbor Vista, CA 93184</div>
  <div class="band slogan">Fabrics That Care</div>
</section>

<section class="card light card-front">
  <div class="brand card-brand"><span class="brand-mark" style="width:16px;height:16px"></span><span class="brand-name">VEL TUNIC</span></div>
  <div class="card-info"><strong>Marcus Pellandrou</strong><br>CEO / Founder<br>805.555.0147<br>marcusp@brightloomwovens.example</div>
  <div class="thin"></div>
</section>

<section class="card dark card-detail">
  <div class="brand card-brand"><span class="brand-mark" style="width:16px;height:16px"></span><span class="brand-name">VEL TUNIC</span></div>
  <div class="card-info"><strong>Marcus Pellandrou</strong><br>CEO / Founder<br>482 Folwell Lane Suite B217<br>Harbor Vista, CA 93184</div>
  <div class="band slogan">Fabrics That Care</div>
</section>

<section class="card light card-blurb">
  <div class="url">www.veltunic.example</div>
  <p>A durable performance base layer that stays fresh<br>and clean through every long shift.</p>
  <div class="band slogan">Fabrics That Care</div>
</section>

<section class="card dark card-back">
  <div class="brand card-brand"><span class="brand-mark" style="width:16px;height:16px"></span><span class="brand-name">VEL TUNIC</span></div>
  <p>www.veltunic.example<br>A durable performance base layer that stays fresh<br>and clean through every long shift.</p>
  <div class="band slogan">Fabrics That Care</div>
</section>

</body>
</html>
```